Designing a brochures for an educational counseling service provider

We would like a 4 sided design on a 11x8.5 paper, half folded. I have including a sample design we did to give you an idea of what we envision but we welcome creativity to make beautiful looking flyers. Text for the flier is included as well as our logo.
- The most important thing is capturing our audience/market. We will be handing these flies to schools, organizations and individual clients.

www.plorvaeducationalconsultants.example

Target Market(s)

We are targeting international students wanting to study in the U.S and Canada.

Industry/Entity Type

Education

Requirements
Must have
• - Clean and clear
• - Our logo should visible and well placed.
• - Could you the pictures of students, libraries and school buildings or you could use the pictures we already have.
Nice to have
• We would like this to match business cards.

```html
<!DOCTYPE html>
<html lang="en">
<head>
<meta charset="utf-8">
<title>Plorva International Educational Consultants – Brochure</title>
<link href="https://fonts.googleapis.com/css2?family=Arimo:ital,wght@0,400;0,700;1,700&display=swap" rel="stylesheet">
<style>
  :root{
    --orange:#f08a1c;
    --orange-soft:#f6a54a;
    --navy:#17237a;
    --blue:#2747a8;
    --ink:#1d1d2b;
    --paper:#ffffff;
    --stage:#e6e6e8;
  }
  *{box-sizing:border-box;margin:0;padding:0}
  html,body{width:1200px;height:800px;overflow:hidden;background:var(--stage);font-family:"Arimo",Arial,sans-serif;color:var(--ink)}
  .spread{position:absolute;top:176px;width:580px;height:448px;display:flex;box-shadow:0 4px 14px rgba(0,0,0,.18)}
  .spread--outside{left:10px}
  .spread--inside{left:610px}
  .page{position:relative;width:290px;height:448px;background:var(--paper);overflow:hidden}
  .page + .page{border-left:1px solid #ddd}
  .swoosh{position:absolute;left:0;width:290px}
  .photo{position:absolute}

  /* back cover */
  .back .swoosh--top{top:0;height:200px}
  .back .photo--students{left:0;top:196px;width:290px;height:120px;background:linear-gradient(135deg,#8c6b4c,#c99a6a 45%,#6d8a52);border-bottom:14px solid var(--orange-soft)}
  .contact{position:absolute;right:18px;top:336px;text-align:right;font-size:7.6px;line-height:1.35}
  .contact h3{font-size:11px;font-weight:400;letter-spacing:.3px;margin-bottom:3px}
  .contact-band{position:absolute;left:0;bottom:18px;width:290px;height:44px;background:linear-gradient(90deg,rgba(39,71,168,0) 0%,var(--blue) 35%,var(--navy));color:#fff;text-align:right;padding:6px 18px 0 0;font-size:7.4px;line-height:1.5}

  /* front cover */
  .front .brand{position:absolute;left:38px;top:38px;display:flex;align-items:center;gap:8px}
  .brand-dot{width:22px;height:22px;border-radius:50%;background:var(--orange)}
  .brand-name{font-size:12px;font-weight:700;color:var(--navy);line-height:1.05;letter-spacing:.3px}
  .front .swoosh--mid{top:80px;height:90px}
  .front .photo--group{left:0;top:150px;width:290px;height:130px;background:linear-gradient(120deg,#6d4a38,#c38b66 40%,#d9a57e 60%,#3b7f8f);border-bottom:14px solid var(--orange-soft);border-radius:0 0 60% 20%/0 0 30px 12px}
  .front .swoosh--low{top:282px;height:40px}
  .tagline{position:absolute;left:20px;right:20px;top:328px;text-align:center;font-size:9.6px;line-height:1.3}
  .services-icons{position:absolute;left:14px;right:14px;top:368px;display:flex;justify-content:space-between}
  .service-icon{width:62px;text-align:center;font-size:6.4px}
  .service-icon svg{display:block;margin:0 auto 4px}

  /* inside left */
  .about .swoosh--top{top:0;height:120px}
  .about .photo--campus{left:172px;top:18px;width:106px;height:106px;border-radius:50%;border:4px solid #555;background:radial-gradient(circle at 50% 35%,#9cb37a,#5e8a3a 60%,#3f6a2a)}
  .about-text{position:absolute;left:16px;top:132px;width:258px;font-size:7px;line-height:1.45}
  .about-text h2{font-size:10px;font-weight:700;color:var(--blue);margin-bottom:3px}
  .about .photo--classroom{left:0;top:246px;width:290px;height:202px;background:linear-gradient(160deg,#b59a7a,#d8c4a4 45%,#6a4a6e 80%,#4a3350)}

  /* inside right */
  .services .swoosh--top{top:0;height:60px}
  .services .swoosh--bottom{bottom:0;height:40px}
  .services-text{position:absolute;left:16px;top:50px;width:262px;font-size:5.9px;line-height:1.34}
  .services-text h2{font-size:8.6px;font-weight:700;font-style:italic;color:var(--blue);margin-top:5px}
  .services-text h4{font-size:6.2px;font-weight:700;font-style:italic;color:var(--blue)}
  .services-text ul{list-style:none}
  .services-text li::before{content:"● ";font-size:5px}
  .services-text strong{font-weight:700}
</style>
</head>
<body>

<section class="spread spread--outside">
  <article class="page back">
    <svg class="swoosh swoosh--top" viewBox="0 0 290 200" preserveAspectRatio="none" aria-hidden="true">
      <path d="M290 0 L290 20 C240 70 200 150 0 170 L0 150 C170 130 230 70 270 0 Z" fill="var(--orange)"/>
      <path d="M0 120 C90 118 150 100 200 60 C160 110 100 140 0 150 Z" fill="var(--blue)"/>
      <path d="M0 126 C70 124 120 112 170 86 C130 118 80 136 0 142 Z" fill="var(--navy)"/>
    </svg>
    <div class="photo photo--students" role="img" aria-label="Photo of three smiling students outdoors on campus"></div>
    <div class="contact">
      <h3>CONTACT US:</h3>
      <p>Executive Director &amp; Independent</p>
      <p>Educational Consultant</p>
      <p>Plorva International Educational Consultants</p>
      <p>418 Maple Ridge Rd</p>
      <p>Suite 12, Fairview, TX</p>
    </div>
    <div class="contact-band">
      <p>Phone: 555-0142</p>
      <p>Email: info@plorvaeducational.example</p>
      <p>www.plorvaeducationalconsultants.example</p>
    </div>
  </article>

  <article class="page front">
    <svg class="swoosh" style="top:0;height:60px" viewBox="0 0 290 60" preserveAspectRatio="none" aria-hidden="true">
      <path d="M0 0 L30 0 C20 20 10 40 0 50 Z" fill="var(--orange)"/>
    </svg>
    <div class="brand">
      <span class="brand-dot"></span>
      <span class="brand-name">PLORVA<br>INTERNATIONAL EDUCATIONAL CONSULTANTS</span>
    </div>
    <svg class="swoosh swoosh--mid" viewBox="0 0 290 90" preserveAspectRatio="none" aria-hidden="true">
      <path d="M0 10 C60 60 160 70 290 40 L290 50 C170 84 60 76 0 24 Z" fill="var(--orange)"/>
      <path d="M80 56 C160 66 230 40 290 0 L290 30 C230 66 160 76 80 56 Z" fill="var(--navy)"/>
    </svg>
    <div class="photo photo--group" role="img" aria-label="Photo of a smiling group of five diverse students"></div>
    <svg class="swoosh swoosh--low" viewBox="0 0 290 40" preserveAspectRatio="none" aria-hidden="true">
      <path d="M0 6 C80 30 180 26 290 10 L290 16 C180 36 80 40 0 22 Z" fill="var(--navy)"/>
    </svg>
    <p class="tagline">A full-services international educational consulting international group serving students and families across the globe.</p>
    <div class="services-icons">
      <div class="service-icon">
        <svg width="30" height="30" viewBox="0 0 30 30" aria-hidden="true"><circle cx="15" cy="15" r="15" fill="var(--orange)"/><path d="M8 11 L15 7 L22 11 Z M9 12 H21 V13 H9 Z M10 14 H12 V20 H10 Z M14 14 H16 V20 H14 Z M18 14 H20 V20 H18 Z M8 21 H22 V23 H8 Z" fill="#fff"/></svg>
        Boarding Schools
      </div>
      <div class="service-icon">
        <svg width="30" height="30" viewBox="0 0 30 30" aria-hidden="true"><circle cx="15" cy="15" r="15" fill="var(--orange)"/><rect x="9" y="8" width="11" height="14" fill="none" stroke="#fff" stroke-width="1.5"/><path d="M12 18 L21 9" stroke="#fff" stroke-width="1.8"/></svg>
        College Admission
      </div>
      <div class="service-icon">
        <svg width="30" height="30" viewBox="0 0 30 30" aria-hidden="true"><circle cx="15" cy="15" r="15" fill="var(--orange)"/><path d="M9 12 A7 7 0 0 1 21 11 M21 18 A7 7 0 0 1 9 19" fill="none" stroke="#fff" stroke-width="1.8"/><path d="M19 8 L22 11 L18 12 Z M11 22 L8 19 L12 18 Z" fill="#fff"/></svg>
        Transfer Students
      </div>
      <div class="service-icon">
        <svg width="30" height="30" viewBox="0 0 30 30" aria-hidden="true"><circle cx="15" cy="15" r="15" fill="var(--orange)"/><path d="M6 12 L15 8 L24 12 L15 16 Z" fill="#fff"/><path d="M10 14 V19 C13 21 17 21 20 19 V14 L15 16 Z" fill="#fff"/></svg>
        Graduate Students
      </div>
    </div>
  </article>
</section>

<section class="spread spread--inside">
  <article class="page about">
    <svg class="swoosh swoosh--top" viewBox="0 0 290 120" preserveAspectRatio="none" aria-hidden="true">
      <path d="M0 60 C80 30 170 12 290 10 L290 16 C170 20 80 40 0 70 Z" fill="var(--orange)"/>
      <path d="M0 74 C70 48 130 34 180 28 C120 44 60 68 0 96 Z" fill="var(--navy)"/>
    </svg>
    <div class="photo photo--campus" role="img" aria-label="Photo of students relaxing on a campus lawn"></div>
    <div class="about-text">
      <h2>ABOUT US:</h2>
      <p>Our mission is to make quality education accessible and affordable to the families we serve. Our services are designed with the needs of each student in mind. Whether one is seeking a boarding school or a university, it is important to find a school whose values are the same as those of our families. With over 10 years of experience, our consultants use profiles created by the ever growing network of schools and work with families to map out the best educational options.</p>
    </div>
    <div class="photo photo--classroom" role="img" aria-label="Photo of students studying in a bright classroom"></div>
  </article>

  <article class="page services">
    <svg class="swoosh swoosh--top" viewBox="0 0 290 60" preserveAspectRatio="none" aria-hidden="true">
      <path d="M60 20 C150 8 230 4 290 0 L290 14 C220 10 150 14 60 24 Z" fill="var(--navy)"/>
      <path d="M0 30 C100 14 200 14 290 26 L290 36 C200 26 100 26 0 36 Z" fill="var(--orange)"/>
    </svg>
    <div class="services-text">
      <h2>SERVICES:</h2>
      <p>Finding the right school or program for your child is one of the most important decisions your family will make. The right choice will make a major impact on your child's future.</p>
      <h4>Our package includes:</h4>
      <ul>
        <li>Intake interview.</li>
        <li>Present range of options based on needs and goals of the family.</li>
        <li>Interview coaching.</li>
        <li>Assistance with application and essays.</li>
        <li>Updates on student progress throughout their enrollment with the school.</li>
        <li>Advisement on financial documents and visa applications.</li>
      </ul>
      <h2>BOARDING SCHOOLS:</h2>
      <p>Students who want the best out of their grade school experience are likely to choose boarding schools because they are proven to better prepare students for university. North American boarding schools provide a quality dynamic experience that will facilitate personal growth in independence, leadership, and confidence as well as provide the academic curriculum necessary to prepare students for university.</p>
      <h2>COLLEGE ADMISSION:</h2>
      <p>As Educational Consultants, we specialize in college/university admissions and we understand how confusing, time-consuming, and stressful the application process can be. Our experienced counselors are here to answer your questions and guide you step by step. As Parents and students may have limited access to information on schools, may not know or understand the entire process as a whole, nor where/how to begin, our experts counselors have a solutions.</p>
      <p>Clients increase the odds of admissions with our comprehensive plan of action. We believe that regardless of a student's level of involvement in extra-curricular activities or preparedness, they still possess something they can offer to the university; therefore we help them shine on their college applications.</p>
      <h2>TRANSFER STUDENTS:</h2>
      <p>Need to find a school an alternative school that is a better match for you? We work with students and families to transfer from one school to another.</p>
      <h2>SCHOLARSHIPS:</h2>
      <p>Funding the education for your children in some of the world's top schools can be very expensive as tuition and fees increase at an average of 4% every year. We work with you to determine the budget for your family, applying to scholarship available and guide you through the financial aid process.</p>
      <p>Over <strong>70%</strong> of our clients have been awarded scholarships or Financial Aid, making your education goals attainable an affordable and your children education possible.</p>
      <p><strong>"Our consultants are members of CEA, the leading association for educational consultants in North America."</strong></p>
    </div>
    <svg class="swoosh swoosh--bottom" viewBox="0 0 290 40" preserveAspectRatio="none" aria-hidden="true">
      <path d="M0 26 C100 20 200 14 290 4 L290 12 C200 22 100 28 0 32 Z" fill="var(--orange)"/>
      <path d="M0 32 C100 28 200 22 290 14 L290 40 L0 40 Z" fill="var(--navy)"/>
    </svg>
  </article>
</section>

</body>
</html>
```